Corrigan & Hale, LLC
Business Cards & Stationery
Corrigan & Hale, LLC -
Creative Brief
Professional
Deborah L. Corrigan
Attorney At Law
418 W. Brookfield Avenue Suite 3B Pearl River, New York 10965-2274
dcorrigan@corriganandhale-example.com
www.corriganandhale-example.com
We will need to be able to use template for other people in the firm.
Specializing in Civil Litigation, Wills, Trusts & Estates, Guardianships, and related matters

```html
<!DOCTYPE html>
<html lang="en">
<head>
<meta charset="utf-8">
<title>Corrigan &amp; Hale, LLC — Business Card</title>
<link rel="stylesheet" href="https://fonts.googleapis.com/css2?family=Cinzel:wght@500;600&family=PT+Serif:ital,wght@0,400;1,400;1,700&display=swap">
<style>
  :root {
    --bg: #e9e7e3;
    --card: #ffffff;
    --green: #1f6b34;
    --charcoal: #2c2c2e;
    --text: #3a3a3a;
    --rule: #9a9a9a;
  }
  * { margin: 0; padding: 0; box-sizing: border-box; }
  html, body {
    width: 1200px; height: 780px; overflow: hidden;
    background: var(--bg);
  }
  .card {
    position: absolute; left: 60px; top: 80px;
    width: 1080px; height: 620px;
    background: var(--card);
    border-radius: 28px;
    overflow: hidden;
    box-shadow: 0 6px 24px rgba(0,0,0,.18);
    font-family: "PT Serif", Georgia, serif;
    color: var(--text);
  }
  .card-swooshes { position: absolute; inset: 0; }
  .brand-mark {
    position: absolute; left: 130px; top: 96px;
    width: 86px; height: 86px;
    background: var(--green);
  }
  .firm-name {
    position: absolute; left: 250px; top: 100px;
    font-family: "Cinzel", "Times New Roman", serif;
    font-weight: 600; font-size: 44px; letter-spacing: 1px;
    color: var(--green);
    white-space: nowrap;
  }
  .firm-rule {
    position: absolute; left: 252px; top: 166px;
    width: 540px; height: 2px; background: var(--rule);
  }
  .firm-tagline {
    position: absolute; left: 470px; top: 174px;
    font-family: "Cinzel", "Times New Roman", serif;
    font-weight: 500; font-size: 18px; letter-spacing: 3px;
    color: var(--charcoal);
    white-space: nowrap;
  }
  .person {
    position: absolute; right: 530px; top: 342px;
    text-align: right; font-size: 21px; line-height: 1.34;
    white-space: nowrap;
  }
  .person-name {
    font-style: italic; font-weight: 700; font-size: 29px;
    color: var(--green); margin-bottom: 4px;
  }
  .divider {
    position: absolute; left: 572px; top: 340px;
    width: 2px; height: 190px; background: var(--rule);
  }
  .contacts {
    position: absolute; left: 594px; top: 350px;
    list-style: none; font-size: 19px;
  }
  .contacts li {
    display: flex; align-items: center; gap: 10px;
    height: 34px; white-space: nowrap;
  }
  .contacts svg { width: 20px; height: 20px; flex: none; }
</style>
</head>
<body>
  <div class="card">
    <svg class="card-swooshes" viewBox="0 0 1080 620" aria-hidden="true">
      <path d="M840,0 L870,0 C985,90 1055,240 1080,460 L1080,505 C1050,275 975,100 840,0 Z" fill="var(--charcoal)"/>
      <path d="M885,0 L1080,0 L1080,420 C1060,235 990,90 885,0 Z" fill="var(--green)"/>
      <path d="M0,335 C50,480 190,585 400,620 L362,620 C190,588 60,492 0,382 Z" fill="var(--charcoal)"/>
      <path d="M0,402 C60,512 180,592 330,620 L0,620 Z" fill="var(--green)"/>
    </svg>

    <div class="brand-mark"></div>
    <div class="firm-name">Corrigan &amp; Hale, LLC</div>
    <div class="firm-rule"></div>
    <div class="firm-tagline">ATTORNEYS AT LAW</div>

    <div class="person">
      <div class="person-name">Deborah L. Corrigan</div>
      <div>Attorney At Law</div>
      <div>418 W. Brookfield Avenue</div>
      <div>Suite 3B, Maple Hollow</div>
      <div>New York 10987-2274</div>
    </div>

    <div class="divider"></div>

    <ul class="contacts">
      <li>
        <svg viewBox="0 0 24 24"><path fill="var(--charcoal)" d="M6.6 10.8a15 15 0 0 0 6.6 6.6l2.2-2.2c.3-.3.7-.4 1-.2 1.1.4 2.3.6 3.6.6.6 0 1 .4 1 1V20c0 .6-.4 1-1 1A17 17 0 0 1 3 4c0-.6.4-1 1-1h3.5c.6 0 1 .4 1 1 0 1.3.2 2.5.6 3.6.1.3 0 .7-.2 1z"/></svg>
        212.555.0148
      </li>
      <li>
        <svg viewBox="0 0 24 24"><rect x="6" y="2" width="12" height="6" fill="var(--charcoal)"/><rect x="3" y="9" width="18" height="9" rx="1" fill="var(--charcoal)"/><rect x="6" y="14" width="12" height="8" fill="var(--charcoal)" stroke="#fff" stroke-width="1.5"/></svg>
        212.555.0173
      </li>
      <li>
        <svg viewBox="0 0 24 24"><circle cx="12" cy="12" r="4" fill="none" stroke="var(--charcoal)" stroke-width="2.4"/><path d="M16 8v5.5c0 1.5 1 2.5 2.2 2.5S21 15 21 12a9 9 0 1 0-3.5 7.1" fill="none" stroke="var(--charcoal)" stroke-width="2.4"/></svg>
        dcorrigan@corriganandhale-example.com
      </li>
      <li>
        <svg viewBox="0 0 24 24"><circle cx="12" cy="12" r="9.5" fill="none" stroke="var(--charcoal)" stroke-width="2"/><ellipse cx="12" cy="12" rx="4" ry="9.5" fill="none" stroke="var(--charcoal)" stroke-width="1.8"/><path d="M2.5 12h19M4 7h16M4 17h16" stroke="var(--charcoal)" stroke-width="1.6"/></svg>
        www.corriganandhale-example.com
      </li>
    </ul>
  </div>
</body>
</html>
```